Business Card/Letterhead Design

We have our Logo, we simply need it cleaned up. Along with a letterhead design. It's pretty simple really.
Instead of the "Corporation" beside the logo. We need it to say "Limited" just under the logo between the "F" and the "Y"
The letter head has to have our address. 2745 Halvorby Crescent Mississauga, ON L4W 3K8 Canada
Reason: I have been called out of town until Monday of next week.
Business
Contact Information for Business Card
2745 Halvorby Crescent Mississauga, ON L4W 3K8 Canada

```html
<!DOCTYPE html>
<html lang="en">
<head>
<meta charset="utf-8">
<title>Norvale Limited – Business Card</title>
<link rel="stylesheet" href="https://fonts.googleapis.com/css2?family=Cinzel:wght@400;600&display=swap">
<style>
  :root {
    --page-bg: #2a2a2c;
    --card-black: #030303;
    --band-blue-light: #4040b4;
    --band-blue-dark: #2b2b8e;
    --silver: #c9c9d2;
    --address-ink: #d6d2ee;
    --brand-blue: #4744b6;
  }
  * { margin: 0; padding: 0; box-sizing: border-box; }
  html, body {
    width: 1200px;
    height: 960px;
    overflow: hidden;
    background: var(--page-bg);
  }
  .canvas {
    position: relative;
    width: 1200px;
    height: 960px;
  }
  .business-card {
    position: absolute;
    left: 100px;
    top: 194px;
    width: 1000px;
    height: 572px;
    border-radius: 34px;
    background: var(--card-black);
    overflow: hidden;
    box-shadow: 0 18px 40px rgba(0,0,0,0.45);
  }
  .address-band {
    position: absolute;
    left: 0; top: 0;
    width: 100%;
    height: 164px;
    background: linear-gradient(90deg, var(--band-blue-dark) 0%, var(--band-blue-light) 55%, var(--band-blue-dark) 100%);
    display: flex;
    align-items: center;
    justify-content: center;
  }
  .address-band::after {
    content: "";
    position: absolute;
    left: 0; bottom: -6px;
    width: 100%;
    height: 6px;
    background: linear-gradient(90deg, #8e8e99, var(--silver) 50%, #8e8e99);
  }
  .address {
    font-family: "Cinzel", serif;
    font-weight: 400;
    font-size: 34px;
    line-height: 1.2;
    letter-spacing: 1px;
    color: var(--address-ink);
    text-align: center;
    font-style: normal;
  }
  .brand {
    position: absolute;
    left: 0;
    top: 170px;
    width: 100%;
    height: 402px;
    display: flex;
    align-items: center;
    justify-content: center;
  }
  .brand-name {
    font-family: "Cinzel", serif;
    font-weight: 600;
    font-size: 78px;
    letter-spacing: 3px;
    color: var(--brand-blue);
  }
</style>
</head>
<body>
  <main class="canvas">
    <section class="business-card">
      <header class="address-band">
        <address class="address">2745 Halvorby Crescent Mississauga,<br>ON L4W 3K8 Canada</address>
      </header>
      <div class="brand">
        <span class="brand-name">Norvale Limited</span>
      </div>
    </section>
  </main>
</body>
</html>
```